Meadowlyn Acres Website Design

We have been redeveloping our website already and are quite happy with the content, but the design needs to be better:
https://harvo-link.example-host.com/

Pages, content, concept etc. Can all be taken from the redeveloped website.
The farmer can register and edit/view their profile, subscribe and these pages need to be designed better as well as contact, about, pricing, tos, privacy and a page with example portlets.

We need a website to appeal to farmers, investors and retiring farmers.

The design should be clean and a little country.

We don't want any repeat designs that some may submit to every project and has no respect for the project brief, so please don't submit them.

Target Market(s)

farmers, investors, retirees

Industry/Entity Type

Farming

Number of Pages Required

5+ page

Colors

Designer to choose colors to be used in the design.

Requirements
Must have
• Nice, clean modern design that is appealing
• Profile page laid out nicely

```html
<!DOCTYPE html>
<html lang="en">
<head>
<meta charset="utf-8">
<title>Meadowlyn Acres – Pricing</title>
<link rel="stylesheet" href="https://fonts.googleapis.com/css2?family=Arimo:wght@400;700&family=Lato:wght@300;400;700&display=swap">
<style>
:root{
  --green:#2fa84a;
  --teal:#11a393;
  --ink:#1c1c1c;
  --muted:#9a9a9a;
  --line:#d8d8d8;
  --white:#ffffff;
  --field-top:#aab39c;
  --field-bottom:#6f7a45;
}
*{box-sizing:border-box;margin:0;padding:0}
html,body{width:1200px;height:3249px;overflow:hidden;background:var(--white)}
body{position:relative;font-family:"Lato",Arial,sans-serif;color:var(--ink)}
.abs{position:absolute}

/* header */
.utility{top:26px;left:0;width:1200px;display:flex;justify-content:center;align-items:center;gap:12px}
.social-dot{width:17px;height:17px;border-radius:50%;background:var(--green)}
.pill-donate{margin-left:14px;background:var(--green);color:var(--white);font-size:16px;padding:5px 16px;border-radius:16px}
.brand{top:78px;left:32px;display:flex;align-items:center;gap:12px;font-size:27px;font-weight:400}
.brand-mark{width:34px;height:34px;border-radius:50%;border:3px solid var(--green)}
.main-nav{top:88px;left:372px;display:flex;gap:26px;font-size:16px;align-items:center}
.main-nav .current{border-bottom:2px solid var(--ink);padding-bottom:2px}
.login{top:82px;left:1078px;width:88px;height:36px;border:2px solid var(--green);border-radius:18px;color:var(--green);font-size:17px;display:flex;align-items:center;justify-content:center}

.page-title{top:180px;left:0;width:1200px;text-align:center;font-family:"Arimo",Arial,sans-serif;font-weight:700;font-size:66px;color:var(--green);letter-spacing:1px}

/* plans */
.plan{border:2px solid var(--line);background:var(--white)}
.plan-name{font-family:"Arimo",Arial,sans-serif;font-weight:700;color:var(--green);font-size:28px;text-align:center;margin-top:18px}
.plan-price{font-family:"Arimo",Arial,sans-serif;font-size:38px;text-align:center;margin-top:10px}
.plan-lead{color:var(--green);font-size:16.5px;margin:14px 22px 0}
.features{list-style:none;margin:18px 20px 0 22px;color:var(--muted);font-weight:300;font-size:16.5px;line-height:23px}
.features li{position:relative;padding-left:14px;margin-bottom:16px}
.features li::before{content:"";position:absolute;left:0;top:10px;width:5px;height:5px;border-radius:50%;background:var(--green)}
.features li.highlight{color:var(--green)}
.features a{color:var(--teal);text-decoration:underline}
.register{position:absolute;left:50%;transform:translateX(-50%);bottom:14px;width:164px;height:43px;border-radius:22px;background:var(--green);color:var(--white);font-family:"Arimo",Arial,sans-serif;font-weight:700;font-size:17px;display:flex;align-items:center;justify-content:center}
.plan-wide .plan-lead{text-align:center;margin-top:12px}
.features-row{display:flex;justify-content:space-between;margin:22px 60px 0 80px}
.features-row li{width:300px}

/* photo areas */
.photo-barn{top:1399px;left:0;width:1200px;height:587px;background:linear-gradient(180deg,var(--field-top) 0%,var(--field-bottom) 100%)}
.photo-herd{top:2647px;left:0;width:1200px;height:498px;background:linear-gradient(180deg,var(--field-top) 0%,var(--field-bottom) 100%)}

/* match fees */
.fees{top:2036px;left:80px;width:1040px}
.fees h2{font-family:"Arimo",Arial,sans-serif;font-weight:700;color:var(--green);font-size:29px}
.fees h3{font-family:"Arimo",Arial,sans-serif;font-weight:700;color:var(--green);font-size:19.5px;margin-top:14px}
.fees ul{list-style:none;margin-top:14px;color:var(--muted);font-weight:300;font-size:17px;line-height:23px}
.fees li{position:relative;padding-left:12px;margin-bottom:16px}
.fees li::before{content:"";position:absolute;left:0;top:10px;width:5px;height:5px;border-radius:50%;background:var(--muted)}

/* donate band */
.appeal{top:2365px;left:0;width:1200px;height:282px;background:var(--teal);color:var(--white);text-align:center}
.appeal h2{font-family:"Arimo",Arial,sans-serif;font-weight:700;font-size:50px;margin-top:38px;letter-spacing:.5px}
.appeal p{width:680px;margin:8px auto 0;font-size:19px;font-weight:300;line-height:24px;color:#e6f6f3}
.appeal .donate-now{display:inline-flex;margin-top:22px;width:178px;height:43px;border:2px solid var(--white);border-radius:22px;align-items:center;justify-content:center;font-family:"Arimo",Arial,sans-serif;font-weight:700;font-size:17px}

/* footer */
.copyright{top:3188px;left:26px;font-size:18px}
.footer-links{top:3188px;left:410px;font-size:18px;display:flex;gap:10px}
.footer-links strong{color:var(--green)}
.footer-social{top:3185px;left:992px;display:flex;gap:10px;align-items:center}
.footer-social .pill-outline{margin-left:6px;border:2px solid var(--green);border-radius:16px;color:var(--green);font-size:16px;padding:3px 14px}
</style>
</head>
<body>

<header>
  <div class="abs utility">
    <span class="social-dot"></span><span class="social-dot"></span><span class="social-dot"></span>
    <span class="pill-donate">Donate</span>
  </div>
  <div class="abs brand"><span class="brand-mark"></span>Meadowlyn Acres</div>
  <nav class="abs main-nav">
    <span>Home</span><span>Aspiring Farmers</span><span>Farming Investors</span><span>Retiring Farmers</span><span>Our Blog</span><span class="current">Pricing</span>
  </nav>
  <div class="abs login">Login</div>
</header>

<h1 class="abs page-title">PRICING CHART</h1>

<section class="abs plan" style="top:299px;left:80px;width:333px;height:764px">
  <h2 class="plan-name">STARTER</h2>
  <p class="plan-price">It’s FREE</p>
  <ul class="features" style="margin-top:30px">
    <li>Public profile</li>
    <li>Stories of success</li>
    <li>Tips on how to get farm ready</li>
    <li>Part of a movement of new farmers across Australia</li>
    <li>Updates on farm opportunities</li>
    <li class="highlight">Eligible for only 1 farm opportunity per year</li>
  </ul>
  <span class="register">Register &gt;</span>
</section>

<section class="abs plan" style="top:299px;left:433px;width:334px;height:764px">
  <h2 class="plan-name">ASPIRING FARMER</h2>
  <p class="plan-price">$ 150/year</p>
  <p class="plan-lead">All of free membership as well as:</p>
  <ul class="features">
    <li>Eligible for farm opportunities</li>
    <li>We help find you great education, training and job opportunities (at discounted rates)</li>
    <li>Support in finding your own dream farm through a retiring farmer you know</li>
    <li>Free <a>Tallyfield market analysis</a> membership (valued at $300 pa)</li>
    <li>Farm business webinars (valued at $200)</li>
    <li>Corporate Partner Opportunities</li>
    <li>Public or Private profile (as required)</li>
    <li>Eligible to enter competitions and win prizes</li>
  </ul>
  <span class="register">Register &gt;</span>
</section>

<section class="abs plan" style="top:299px;left:788px;width:333px;height:764px">
  <h2 class="plan-name">FARM READY</h2>
  <p class="plan-price">$ 400/year</p>
  <ul class="features" style="margin-top:24px">
    <li>All of Aspiring Farmer as well as</li>
    <li>We promote your profile on our blog and social media</li>
    <li>4 half hour phone sessions with the Meadowlyn Acres team to help you get farm-ready</li>
    <li>We review your profile and offer tips for improvement</li>
    <li>We review your education requirements and find you the best next opportunities</li>
    <li>You will be selected for any publicity opportunities that arise</li>
    <li>Profile promotion on home page for 3 months of the year</li>
    <li class="highlight">Meadowlyn Acres team on tap for advice</li>
    <li class="highlight">We will find you a farm mentor</li>
  </ul>
  <span class="register">Register &gt;</span>
</section>

<section class="abs plan plan-wide" style="top:1085px;left:80px;width:1041px;height:289px">
  <h2 class="plan-name">INVESTORS AND RETIREES</h2>
  <p class="plan-price">It’s FREE</p>
  <p class="plan-lead">All of free membership as well as:</p>
  <ul class="features features-row">
    <li>Support in negotiating farm opportunities</li>
    <li>Corporate partner opportunities</li>
    <li>Any other great deals we can find</li>
  </ul>
  <span class="register">Register &gt;</span>
</section>

<div class="abs photo-barn" role="img" aria-label="Photo area: hay bales stored under an open farm shed in a paddock"></div>

<section class="abs fees">
  <h2>MATCH MAKING FEES</h2>
  <h3>We will charge a success fee for when you are matched on your farm:</h3>
  <ul>
    <li>Aspiring farmer - You will be charged a match-making fee upon the successful placement onto your farm. Depending on the arrangement, this will be a maximum of $2,000.</li>
    <li>Investor – if you need farmers, we charge a fee to find the farmer you need. This can be as involved or hands off as you require. Our only requirement is that we will be ensuring that the new farmer is able to meet their dreams of farm ownership and management and we will support them through this.</li>
    <li>Retiring farmer – You will be charged a match-making fee upon the successful placement of a new farmer and investors into your farm. Depending on the arrangement, this will be a maximum of $5,000</li>
  </ul>
</section>

<section class="abs appeal">
  <h2>HELP US MAKE THIS A REALITY</h2>
  <p>If you want to rejuvenate regional Australia then consider donating to us. We will love you forever and any donation over $50 we will get an aspiring farmer to write you a personalised message</p>
  <span class="donate-now">DONATE NOW</span>
</section>

<div class="abs photo-herd" role="img" aria-label="Photo area: cattle grazing in a valley paddock with a rider on horseback"></div>

<footer>
  <p class="abs copyright">© Meadowlyn Acres 2017</p>
  <p class="abs footer-links"><span><strong>Support:</strong> Contact</span><span>|</span><span>Terms of Service</span><span>|</span><span>Privacy</span><span>|</span><span>Newsletter</span></p>
  <div class="abs footer-social">
    <span class="social-dot"></span><span class="social-dot"></span><span class="social-dot"></span>
    <span class="pill-outline">Donate</span>
  </div>
</footer>

</body>
</html>
```